Billboard ad

We need graphics for a 35ft billboard x 8ft that will be used around the world for us.
Please use the words such as, but not limited to "Buying, Selling or Renting, go to kelbranest.com. please use the graphic from our website with the picture of the marrick tower, etc or any other similar graphic you feel would suit... , and our logo, Please note, wiords such as dreamhome, investment, holidays etc... can also be used.

Investment

```html
<!DOCTYPE html>
<html lang="en">
<head>
<meta charset="utf-8">
<title>Kelbranest Billboard</title>
<link rel="stylesheet" href="https://fonts.googleapis.com/css2?family=Arimo:wght@400;700&display=swap">
<style>
  :root {
    --bg-grey: #adadad;
    --panel-white: #ffffff;
    --edge-grey: #8a8a8a;
    --ink-dark: #3b3b3b;
    --ink-mid: #555555;
    --brand-green: #7cc242;
    --bar-green: #8dc63f;
    --art-light: #c9cbc4;
    --art-mid: #a9b59a;
    --white: #ffffff;
  }
  * { margin: 0; padding: 0; box-sizing: border-box; }
  html, body { width: 1200px; height: 275px; overflow: hidden; background: var(--white); }
  body { font-family: "Arimo", Arial, sans-serif; }

  .billboard {
    position: relative;
    width: 1200px;
    height: 275px;
    background: var(--bg-grey);
    overflow: hidden;
  }
  .corner-panel { position: absolute; inset: 0; }

  .site-url {
    position: absolute;
    left: 20px; top: 18px;
    font-size: 11px; font-weight: 700;
    letter-spacing: 1px;
    color: var(--ink-dark);
  }

  .hero-art {
    position: absolute;
    left: 60px; top: 36px;
    width: 335px; height: 206px;
    border-radius: 24px;
    background: linear-gradient(180deg, var(--art-mid) 0%, var(--art-light) 100%);
    opacity: .85;
  }

  .headline {
    position: absolute;
    left: 414px; top: 100px;
    font-size: 40px; font-weight: 400;
    line-height: 46px;
    color: var(--ink-dark);
    text-transform: uppercase;
    white-space: nowrap;
  }

  .services {
    position: absolute;
    left: 760px; top: 203px;
    font-size: 19px;
    color: var(--white);
    white-space: nowrap;
  }

  .brand {
    position: absolute;
    left: 930px; top: 34px;
    display: flex; align-items: center; gap: 8px;
  }
  .brand-dot {
    width: 18px; height: 18px;
    border-radius: 50%;
    background: var(--brand-green);
  }
  .brand-name {
    font-size: 34px; font-weight: 700;
    color: var(--ink-mid);
    letter-spacing: -0.5px;
  }

  .offer-bar {
    position: absolute;
    left: 0; top: 248px;
    width: 436px; height: 20px;
    background: var(--bar-green);
  }
  .offer-line {
    position: absolute;
    left: 16px; top: 248px;
    height: 20px;
    display: flex; align-items: center;
    font-size: 10px; font-weight: 700;
    color: var(--ink-dark);
    white-space: nowrap;
  }
  .price-badge {
    position: relative;
    width: 34px; height: 26px;
    margin: 0 10px 0 6px;
    display: flex; align-items: center; justify-content: center;
  }
  .price-badge svg { position: absolute; inset: 0; }
  .price-badge span { position: relative; font-size: 9.5px; color: var(--ink-dark); }
</style>
</head>
<body>
<main class="billboard">
  <svg class="corner-panel" width="1200" height="275" viewBox="0 0 1200 275" aria-hidden="true">
    <path d="M858 0 C840 45 905 105 1010 150 C1110 195 1160 235 1200 262 L1200 0 Z" fill="var(--edge-grey)"/>
    <path d="M872 0 C856 42 918 100 1020 143 C1115 185 1165 222 1200 246 L1200 0 Z" fill="var(--panel-white)"/>
  </svg>

  <p class="site-url">www.kelbranest.com</p>

  <div class="hero-art" role="img" aria-label="Illustration: floating island with Marrick Tower and world landmarks among clouds and hot-air balloons"></div>

  <h1 class="headline">Get the best value<br>with property investment.</h1>

  <p class="services">Buying, Selling or Renting,</p>

  <div class="brand">
    <span class="brand-dot"></span>
    <span class="brand-name">kelbranest</span>
  </div>

  <div class="offer-bar"></div>
  <p class="offer-line">
    List your property on the largest online global property marketplace for only
    <span class="price-badge">
      <svg viewBox="0 0 34 26" aria-hidden="true"><polygon points="17,1 33,13 17,25 1,13" fill="var(--white)"/></svg>
      <span>$99.</span>
    </span>
    for more info Call, 555 014 2290
  </p>
</main>
</body>
</html>
```